Brindle Outcomes WebDesign

Although the designs we have had are great we are looking for something unique and would like to move away from the traditional. We append additional comments and files to reflect this. WE are looking for designs to showcase there artistic flare.

Task
To design Brindle Outcomes home page and a second page ie information on our Internet Marketing Services

Client:
Brindle Outcomes is the next generation provider of international marketing, branding, design, Search Engine Optimization(SEO) and Search Engine Marketing(SEM). Utilising a variety of crowd-source channels and trust networks, Brindle Outcomes is able to offer you a complete internet marketing package. From initial design and branding to the continued work on SEO all our services are geared towards dramatically increasings your revenues. Our primary goal is to build greater trading bridges between English-speaking and Chinese-speaking worlds. We believe that a true understanding of the local market is only achievable if you are a native speaker. The power of our networks and processes have been focused to enable Brindle Outcomes to enlist only native speakers to bolster your Internet Marketing Campaign.

The primary color pallet is:

FF9571
B23308
FF6633
858585
BDBDBD
or
https://palettes.vormix.example/#themes/search?term=brindle%20outcomes

Sites we like
http://www.trevonix.example/
http://www.morbela.example/
Updates

We have believe that we will need to push our design packages (outsourced through artflockly) more. We would like this to be reflected on the front page.

This means that the menu should also include

Design
Also the use of content management system wendix

Have added a few more sites that we like
www.harbourpixelstudio.example.hk
www.qmt.example.hk

Really excited with all the designs so far.  We would like the design to move away from the more standard layout. With this in mind we would like to see some design that feature hexagons, or decagons.
Please feel free to let loose! we want a design that is quit unique

We have included to vector files.

vector file 8016151 is for a color reference we thik that in order to enhence the design we need to expand the color palette, would want to maintain the primary corporate colors, but include some bright additional colors.

The second was our insipration for the the hexagon. expanding on the idea we thought that the main menu could be made up of hexagons. The ad/info modules that appear half way up the page be similar to those in the vector.

Reason: Have updated brief and are looking for a more unique feel to the design.

Target Market(s)

Small to medium business looking to branch out further in the international market

Industry/Entity Type

Internet

Requirements
Must have
• A login/search section
A separate floating feedback tab
Main Navigation – Home, Internet Marketing, Cloud Computing
A banner space from informative text on our services
Must have a request for a quote on each page

```html
<!DOCTYPE html>
<html lang="en">
<head>
<meta charset="utf-8">
<title>Brindle Outcomes – SEO and Cloud Consultant</title>
<link href="https://fonts.googleapis.com/css2?family=Ubuntu:ital,wght@0,400;0,500;0,700;1,400&family=Arimo:wght@400&display=swap" rel="stylesheet">
<style>
:root{
  --orange:#f05a22;
  --orange-band:#ef5f25;
  --orange-soft:#ff9571;
  --rust:#b23308;
  --ink:#1c1c1c;
  --text:#333;
  --grey:#858585;
  --grey-light:#bdbdbd;
  --paper:#f4f4f4;
  --white:#fff;
  --dark:#3b3b3b;
  --link:#2a7fb8;
  --hero-blue:#2d8fd8;
}
*{box-sizing:border-box;margin:0;padding:0}
html,body{width:1007px;height:1200px;overflow:hidden}
body{position:relative;background:var(--paper);font-family:"Ubuntu",sans-serif;color:var(--text)}
.abs{position:absolute}

/* top bar */
.topbar{left:0;top:0;width:1007px;height:27px;background:var(--dark);border-top:3px dashed var(--orange)}
.topbar a{position:absolute;right:119px;top:5px;color:#eee;font-size:10px;font-weight:500;text-decoration:none}
.topbar-rule{left:0;top:27px;width:1007px;height:2px;background:var(--orange)}

/* header */
.header{left:0;top:29px;width:1007px;height:83px;background:linear-gradient(#fafafa,#ececec);border-bottom:1px solid #ddd}
.brand{display:flex;align-items:center;gap:14px}
.brand-mark{width:60px;height:60px;border:5px solid var(--orange);border-radius:50%;flex:none}
.brand-name{font-size:24px;font-weight:700;color:var(--orange);letter-spacing:-.5px;line-height:1;white-space:nowrap}
.brand-sub{font-size:10.5px;color:var(--ink)}
.vrule{width:1px;background:#f2b59c}
.tagline{left:484px;top:50px;width:220px;text-align:center;font-size:14px;color:var(--ink);line-height:1.4}
.tagline b{font-weight:400;color:var(--orange)}
.tagline .big{font-size:18px}
.mainnav{left:776px;top:43px;width:120px;list-style:none}
.mainnav li{height:19px;font-size:11.5px;color:var(--ink);padding-left:12px;position:relative;line-height:16px}
.mainnav li::before{content:"";position:absolute;left:3px;top:5px;border:3px solid transparent;border-left:4px solid #888}
.mainnav li.current{background:var(--orange);color:#fff}
.mainnav li.current::before{border-left-color:#fff}

/* hero */
.hero-title{left:122px;top:170px;line-height:1}
.hero-title .l1{font-size:33px;font-weight:700;color:var(--orange);display:block;letter-spacing:-.5px}
.hero-title .l2{font-size:28.5px;font-weight:700;color:var(--ink);display:block;letter-spacing:-.8px;margin-top:2px}
.hero-copy{left:122px;top:248px;width:240px;font-size:10.4px;line-height:13.3px;color:var(--ink)}
.hero-list{left:368px;top:249px;list-style:none;font-size:9.6px;color:var(--ink)}
.hero-list li{height:17px;padding-left:14px;position:relative}
.hero-list li::before{content:"»";position:absolute;left:0;top:-3px;color:var(--orange);font-size:13px;font-weight:700}
.btn-details{left:367px;top:318px;width:121px;height:30px;background:var(--orange);color:#fff;font-size:14px;font-weight:500;display:flex;align-items:center;gap:8px;padding-left:10px;box-shadow:0 2px 3px rgba(0,0,0,.25)}
.btn-details i{width:16px;height:16px;border-radius:50%;background:#fff;color:var(--orange);font-style:normal;font-size:11px;line-height:15px;text-align:center;font-weight:700}
.hero-art{left:528px;top:128px;width:362px;height:296px;border-radius:6px;
  background:linear-gradient(135deg,#ffb08a 0%,#7cc4f0 35%,#2d8fd8 60%,#283a6e 100%);opacity:.9}
.slider-dots{left:462px;top:387px;width:87px;height:21px;background:#8a8a8a;display:flex;gap:6px;align-items:center;justify-content:center}
.slider-dots span{width:11px;height:11px;border-radius:50%;background:#fff}
.slider-dots span.on{background:var(--orange)}
.hero-shadow{left:240px;top:408px;width:560px;height:30px;background:radial-gradient(ellipse at 50% 0,rgba(0,0,0,.18),rgba(0,0,0,0) 70%)}

/* feedback */
.feedback{left:972px;top:172px;width:35px;height:121px}
.feedback span{position:absolute;left:10px;top:22px;writing-mode:vertical-rl;color:#fff;font-size:12px;letter-spacing:1.5px;font-weight:500}

/* products */
.section-rule{left:0;top:448px;width:1007px;height:4px;border-top:1px solid #cfcfcf;border-bottom:1px solid #cfcfcf}
.section-title{left:0;top:440px;width:1007px;text-align:center}
.section-title span{background:var(--paper);padding:0 8px;font-size:18px;color:var(--orange)}
.service{width:235px}
.service h2{font-size:19px;font-weight:700;color:var(--ink);letter-spacing:.3px}
.service .row{display:flex;gap:9px;margin-top:14px}
.service .ico{width:36px;height:36px;flex:none}
.service p{font-size:8.8px;line-height:11px;color:var(--ink);width:170px}
.service .links{margin:12px 0 0 43px;display:grid;grid-template-columns:66px 100px;row-gap:10px;font-size:8px;color:var(--link)}
.service .links span{position:relative;padding-left:10px}
.service .links span::before{content:"»";position:absolute;left:0;top:-2px;color:var(--orange);font-size:11px;font-weight:700}
.service .more{border-top:1px dotted #aaa;margin-top:11px;padding-top:7px;text-align:right;font-size:10.5px;font-weight:500;color:var(--ink)}
.service .more i{display:inline-block;width:15px;height:15px;border-radius:50%;background:var(--orange);color:#fff;font-style:normal;font-size:10px;line-height:14px;text-align:center;margin-right:5px;vertical-align:-3px}

/* orange band */
.band{left:0;top:662px;width:1007px;height:220px;background:var(--orange-band)}
.band h3{font-size:17px;font-weight:500;color:#fff}
.band .copy{font-size:8.8px;line-height:11px;color:#ffd5c2}
.band .sub{font-size:8px;color:#fff;position:relative;padding-left:11px}
.band .sub::before{content:"»";position:absolute;left:0;top:-2px;font-size:11px;font-weight:700}
.band .divider{width:1px;height:106px;top:44px;background:#c7461a}
.ring{width:42px;height:42px;border:3px solid #fff;border-radius:50%}
.avatar{width:48px;height:48px;border-radius:50%;background:radial-gradient(circle at 50% 40%,#d9a98a,#6b3b25)}
.mission-quote{font-size:12px;font-style:italic;line-height:15.3px;color:#fff;width:185px}
.mission-by{font-size:8.5px;font-weight:500;color:#fff}
.quote-ico{width:42px;height:42px;border-radius:50%;background:#fff;border:3px solid #a8dff0}
.field{background:#fff;font-size:9.5px;color:#333;padding:6px 10px;width:198px}
.submit{background:#111;color:#fff;font-size:9.5px;width:56px;height:18px;text-align:center;line-height:18px}

/* testimonial */
.testimonial{left:108px;top:924px;width:786px;height:90px;background:#fff;box-shadow:0 8px 10px -8px rgba(0,0,0,.25)}
.testimonial h4{position:absolute;top:6px;width:100%;text-align:center;font-size:19px;font-weight:400;color:var(--ink)}
.testimonial h4 b{font-weight:400;color:var(--orange)}
.testimonial p{position:absolute;left:136px;top:40px;width:516px;text-align:center;font-family:"Arimo",sans-serif;font-size:9.9px;line-height:13.5px;color:#222}
.arrow{top:30px;font-size:28px;color:#333;font-weight:300}

/* footer */
.footer{left:0;top:1040px;width:1007px;height:160px}
.fcol{top:1092px;font-size:8px;line-height:9.4px;color:#fff}
.fcol h5{font-size:8.8px;font-weight:400;margin-bottom:3px}
.fdiv{top:1092px;width:1px;height:58px;background:#777}
.footer-brand{left:646px;top:1100px;display:flex;align-items:center;gap:14px}
.footer-brand .brand-mark{width:44px;height:44px;border-width:3px}
.footer-brand .brand-name{font-size:20px;color:#ccc}
.footer-sub{left:725px;top:1129px;font-size:7px;color:#aaa}
.social{left:812px;top:1147px;display:flex;gap:6px}
.social span{width:13px;height:13px;border-radius:50%;background:#bbb}
.copyright{left:722px;top:1175px;font-size:8.5px;color:#aaa}
.bottom-stripe{left:0;top:1196px;width:1007px;height:4px;border-top:4px dashed var(--orange);background:#111}
</style>
</head>
<body>

<div class="abs topbar"><a href="#">Login / Register</a></div>
<div class="abs topbar-rule"></div>

<header class="abs header"></header>
<div class="abs" style="left:122px;top:40px">
  <div class="brand"><span class="brand-mark"></span><span class="brand-name" style="margin-top:-10px">BrindleOutcomes.com</span></div>
</div>
<div class="abs brand-sub" style="left:231px;top:80px">SEO and Cloud Consultant</div>
<div class="abs vrule" style="left:483px;top:44px;height:56px"></div>
<div class="abs tagline">Next Generation <b>Provider</b><br>of <b class="big">Internet Marketing</b></div>
<div class="abs vrule" style="left:704px;top:44px;height:56px"></div>
<ul class="abs mainnav">
  <li class="current">Home</li>
  <li>Internet Marketing</li>
  <li>Cloud Computing</li>
</ul>
<div class="abs vrule" style="left:896px;top:44px;height:56px"></div>

<h1 class="abs hero-title"><span class="l1">A Complete</span><span class="l2">Business Marketing Package</span></h1>
<p class="abs hero-copy">Brindle Outcomes is the next generation provider of international marketing, branding, design, Search Engine Optimization(SEO) and Search Engine Marketing(SEM). Utilising a variety of crowd-source channels and trust networks, Brindle Outcomes is able to offer you a complete internet marketing package.</p>
<ul class="abs hero-list"><li>Branding</li><li>Design Services</li><li>Our Portfolio</li></ul>
<div class="abs btn-details"><i>»</i>View Details</div>
<div class="abs hero-art" role="img" aria-label="Illustration of a laptop with a glowing globe, SEO lettering, gears and a paint palette"></div>
<div class="abs hero-shadow"></div>
<div class="abs slider-dots"><span class="on"></span><span></span><span></span><span></span><span></span></div>

<svg class="abs feedback" viewBox="0 0 35 121" aria-label="Feedback tab">
  <rect x="0" y="0" width="35" height="3" fill="#333"/>
  <rect x="0" y="4" width="35" height="3" fill="#c23a10"/>
  <path d="M0 8H35V121L17.5 110L0 121Z" fill="#f05a22"/>
</svg>
<div class="abs feedback"><span>FEEDBACK</span></div>

<div class="abs section-rule"></div>
<div class="abs section-title"><span>Products &amp; Services</span></div>

<section class="abs service" style="left:122px;top:480px">
  <h2>WEB SERVICES</h2>
  <div class="row">
    <div class="ico" role="img" aria-label="Computer monitor icon" style="background:linear-gradient(#7cc8f0,#2a86c8);border:3px solid #ccc;border-bottom-width:8px"></div>
    <p>Lorem ipsum dolor sit amet, consectetur adipisicing elit, sed do eiusmod tempor incididunt ut labore et dolore magna aliqua.</p>
  </div>
  <div class="links"><span>Web Design</span><span>Identity Design</span><span>Domain Reg</span><span>eCommerce</span></div>
  <div class="more" style="width:204px"><i>›</i>More Web Services</div>
</section>

<section class="abs service" style="left:407px;top:480px">
  <h2>BUSINESS SERVICES</h2>
  <div class="row">
    <div class="ico" role="img" aria-label="Cardboard box icon" style="background:linear-gradient(#e9b67a,#c98a45);width:28px;margin-left:2px"></div>
    <p>Lorem ipsum dolor sit amet, consectetur adipisicing elit, sed do eiusmod tempor incididunt ut labore et dolore magna aliqua.</p>
  </div>
  <div class="links"><span>Web Hosting</span><span>VoIP Services</span><span>Server Host</span><span>Broadband</span></div>
  <div class="more" style="width:216px;margin-left:-4px"><i>›</i>More Business Services</div>
</section>

<section class="abs service" style="left:678px;top:480px">
  <h2>SUPPORT</h2>
  <div class="row">
    <div class="ico" role="img" aria-label="Lifebuoy icon" style="border-radius:50%;border:9px solid #f26a2e;background:#fff"></div>
    <p>Lorem ipsum dolor sit amet, consectetur adipisicing elit, sed do eiusmod tempor incididunt ut labore et dolore magna aliqua.</p>
  </div>
  <div class="links"><span>Our Rates</span><span>Payment Option</span><span>Online Help</span><span>Client Login</span></div>
  <div class="more" style="width:212px"><i>›</i>More Support Services</div>
</section>

<section class="abs band">
  <div class="abs ring" style="left:122px;top:14px"></div>
  <h3 class="abs" style="left:175px;top:23px">About Us</h3>
  <p class="abs copy" style="left:174px;top:55px;width:170px">Lorem ipsum dolor sit amet, consectetur adipisicing elit, sed do eiusmod tempor incididunt ut labore et dolore magna aliqua.</p>
  <div class="abs sub" style="left:173px;top:108px">Company Profile</div>
  <div class="abs sub" style="left:173px;top:129px">Team Profile</div>
  <div class="abs divider" style="left:375px"></div>

  <div class="abs avatar" style="left:405px;top:14px" role="img" aria-label="Portrait photo of the managing director"></div>
  <h3 class="abs" style="left:461px;top:23px">Our Mission</h3>
  <p class="abs mission-quote" style="left:461px;top:52px">“Lorem ipsum dolor sit amet, consectetur adipisicing elit, sed do eiusmod tempor incididunt ut labore et dolore magna aliqua.”</p>
  <div class="abs mission-by" style="left:405px;top:125px">Mara Ellison, Managing Director</div>
  <div class="abs divider" style="left:666px"></div>

  <div class="abs quote-ico" style="left:690px;top:14px">
    <svg width="36" height="36" viewBox="0 0 36 36"><path d="M12 9h9l5 5v13H12z" fill="none" stroke="#2aaed8" stroke-width="2"/><path d="M15 18h8M15 21h8M15 24h6" stroke="#2aaed8" stroke-width="1.5"/></svg>
  </div>
  <h3 class="abs" style="left:745px;top:23px">Request For Quote</h3>
  <div class="abs field" style="left:692px;top:62px;height:23px">Name</div>
  <div class="abs field" style="left:692px;top:91px;height:23px">Email</div>
  <div class="abs field" style="left:692px;top:120px;height:59px">Write Your Message Here...</div>
  <div class="abs submit" style="left:834px;top:184px">Submit</div>
</section>

<section class="abs testimonial">
  <h4>Client <b>Testimonial</b></h4>
  <span class="abs arrow" style="left:92px">‹</span>
  <p>“At vero eos et accusamus et iusto odio dignissimos ducimus qui blanditiis praesentium voluptatum deleniti atque corrupti quos dolores et quas molestias excepturi sint occaecati cupiditate non provident, similique sunt in culpa qui officia deserunt mollitia animAi, id est laborum et dolorum fuga.”</p>
  <span class="abs arrow" style="left:705px">›</span>
</section>

<svg class="abs footer" viewBox="0 0 1007 160" preserveAspectRatio="none">
  <path d="M0 4L1007 40V160H0Z" fill="#3d3d3d"/>
  <path d="M0 3L1007 37V42L0 8Z" fill="#f05a22"/>
</svg>

<div class="abs fcol" style="left:118px"><h5>Company</h5>About Us<br>Portfolio<br>Contact</div>
<div class="abs fdiv" style="left:177px"></div>
<div class="abs fcol" style="left:193px"><h5>Learn More</h5>F.A.Q<br>How it Works<br>Privacy Policy<br>Terms &amp;<br>Conditions</div>
<div class="abs fdiv" style="left:263px"></div>
<div class="abs fcol" style="left:286px"><h5>Internet Marketing Services</h5>Search Engine Marketing and Optimization<br>Social Media Marketing<br>Pay Per Click<br>SEO Resources</div>
<div class="abs fdiv" style="left:463px"></div>
<div class="abs fcol" style="left:482px"><h5>News</h5>Latest News<br>Testimonials</div>
<div class="abs fdiv" style="left:577px"></div>

<div class="abs footer-brand"><span class="brand-mark"></span><span class="brand-name">BrindleOutcomes.com</span></div>
<div class="abs footer-sub">SEO and Cloud Consultant</div>
<div class="abs social" aria-label="Social links"><span></span><span></span><span></span><span></span></div>
<div class="abs copyright">Copyright © 2012 BrindleOutcomes.com</div>
<div class="abs bottom-stripe"></div>

</body>
</html>
```